Brand and Marketing Coach Needs PDF Designed

I have content that i need placed into a simple but great PDF design. The PDF is about the formula I use to build personal brands. This is geared towards entrepreneurs, experts, coaches, therapists, wellness practitioners, and indpendent business owners who serve to improve the lives of others.
The company name is changing from Corvelta Studio to Growth with Neighbors (I don't have that logo yet, so working backwards a bit. For now, the Corvelta Studio logo can be used.) My brand is NOT formal and corporate, but it's also not neon-pink and screaming at you. It's down to earth, hip, a bit modern but warm. It's about no BS and authenticity. The final deliverable should make the reader feel focused, smart, motivated and hopeful.

Target Market(s)

Conscious entrepreneurs and small business owners. this one is specifically for pharmacy entrepreneurs but this will be used for various audiences later.

Font styles to use
Sans Serif

Colors
eaf1f7
3377b5
6b449b
f37122
faa54b
f68e4e
ffc214

Requirements
Must have
• Modern design. colors that match logo - 4e5583 (i think that is the blue.) d65a40.
• Could have these colors as well: c6a254, 01bcc3
• But open to other colors
Nice to have
• I'd like to see some ways to make this PDF simple and readable, and eye-catching. I'd also like to use the uploaded ebooks for design ideas.
Should not have
• neon colors, clip art

```html
<!DOCTYPE html>
<html lang="en">
<head>
<meta charset="utf-8">
<title>The Personal Brand Formula</title>
<link href="https://fonts.googleapis.com/css2?family=League+Gothic&family=Roboto:ital,wght@0,100;0,300;0,700;1,300&family=Roboto+Condensed:wght@300&display=swap" rel="stylesheet">
<style>
  :root {
    --navy: #4e5583;
    --orange: #ff6a00;
    --gold: #c6a254;
    --white: #ffffff;
    --photo-light: #e4e4e4;
    --photo-dark: #5a5a5a;
  }
  html, body {
    margin: 0;
    padding: 0;
    width: 1200px;
    height: 927px;
    overflow: hidden;
    background: var(--white);
  }
  .cover {
    position: relative;
    width: 1200px;
    height: 927px;
    overflow: hidden;
    font-family: "Roboto", sans-serif;
  }
  .hero-photo {
    position: absolute;
    left: 0;
    top: 0;
    width: 1200px;
    height: 456px;
    background:
      radial-gradient(ellipse 260px 300px at 340px 260px, var(--photo-dark) 0%, rgba(90,90,90,0.55) 55%, rgba(90,90,90,0) 100%),
      linear-gradient(90deg, #8c8c8c 0%, #bdbdbd 35%, var(--photo-light) 65%, #f4f4f4 100%);
  }
  .headline {
    position: absolute;
    margin: 0;
    font-family: "League Gothic", sans-serif;
    font-weight: 400;
    line-height: 1;
    text-transform: uppercase;
  }
  .headline span { position: absolute; display: block; white-space: nowrap; }
  .step-word { color: var(--orange); font-size: 178px; letter-spacing: -1px; }
  .step-word.step { left: 684px; top: 2px; }
  .step-word.it { left: 684px; top: 140px; }
  .step-word.up { left: 684px; top: 276px; }
  .noticed { left: 820px; top: 143px; color: var(--navy); font-size: 76px; }
  .amp { left: 803px; top: 196px; color: var(--gold); font-size: 126px; }
  .grow { left: 870px; top: 203px; color: var(--gold); font-size: 61px; }
  .client { left: 858px; top: 251px; color: var(--gold); font-size: 61px; }
  .studio-mark {
    position: absolute;
    left: 920px;
    top: 372px;
    display: flex;
    align-items: center;
    gap: 8px;
    color: var(--navy);
    font-family: "Roboto", sans-serif;
    font-weight: 700;
    font-size: 26px;
  }
  .studio-mark .dot {
    width: 34px; height: 34px; border-radius: 50%;
    background: var(--navy);
  }
  .title-band {
    position: absolute;
    left: 0;
    top: 456px;
    width: 1200px;
    height: 471px;
    background: var(--navy);
  }
  .guide-title {
    position: absolute;
    left: 172px;
    top: 120px;
    margin: 0;
    color: var(--white);
    font-weight: 100;
    font-size: 79px;
    line-height: 1;
    white-space: nowrap;
  }
  .guide-title em { font-style: italic; font-weight: 300; }
  .audience-tag {
    position: absolute;
    left: 174px;
    top: 206px;
    width: 440px;
    height: 39px;
    background: var(--orange);
    clip-path: polygon(0 0, 100% 0, 92% 100%, 0 100%);
    color: var(--white);
    font-weight: 700;
    font-size: 28px;
    line-height: 39px;
    padding-left: 12px;
    box-sizing: border-box;
    white-space: nowrap;
  }
  .guide-summary {
    position: absolute;
    left: 174px;
    top: 296px;
    margin: 0;
    color: var(--white);
    font-family: "Roboto Condensed", sans-serif;
    font-weight: 300;
    font-size: 23px;
    white-space: nowrap;
  }
</style>
</head>
<body>
  <main class="cover">
    <div class="hero-photo" role="img" aria-label="Black and white photo of a woman in a blazer sitting on stone steps, looking to the side"></div>

    <h1 class="headline">
      <span class="step-word step">Step</span>
      <span class="step-word it">It</span>
      <span class="step-word up">Up,</span>
      <span class="noticed">Get Noticed,</span>
      <span class="amp">&amp;</span>
      <span class="grow">Grow Your</span>
      <span class="client">Client Base</span>
    </h1>

    <div class="studio-mark">
      <span class="dot"></span>
      <span class="studio-name">Corvelta Studio</span>
    </div>

    <section class="title-band">
      <h2 class="guide-title">The <em>Personal</em> Brand Formula</h2>
      <div class="audience-tag">For Pharmacy Entrepreneurs</div>
      <p class="guide-summary">The quick n' dirty guide to creating a unique personal brand that attracts your ideal clients.</p>
    </section>
  </main>
</body>
</html>
```